Cedar Ridge Paving. Chip Seal Done Right

I need my card to have all my basic information on it. Keep it simple. Include web site, phone number and email address. Include phrase Chip Seal Done Right or Cedar Ridge’s Top Paving Company. Keep card simple. Include color and logo. Put all contact info on card. Make card simple and not complicated.
Updates

Here is infuriation yo out in business card

Mark T. Delgado
512.408.7316 cell phone
Markdelgado7@mailbrook.net
www.cedarridgepaving.net

Target Market(s)

Hill Country Texas USA

Industry/Entity Type

Road chip seal

Contact Information for Business Card

We chip seal roads for ranches and property owners

Font styles to use
Serif
Sans Serif
Decorative
Script

Colors
0054AA
0677BA
7BADD7
CADEEF
E8F1F8
EB3D1F
EC4F4E
F09395
F8D3D4
FCEDEE

Requirements
Must have
• Keep it simply
Nice to have
• Logo and all basic info

```html
<!DOCTYPE html>
<html lang="en">
<head>
<meta charset="utf-8">
<title>Cedar Ridge Paving – Business Card</title>
<link rel="stylesheet" href="https://fonts.googleapis.com/css2?family=Arimo:wght@400;700&display=swap">
<style>
  :root {
    --navy: #1c2566;
    --red: #b3202e;
    --grey-text: #7a7a7a;
    --rule: #9a9a9a;
    --paper: #ffffff;
    --backdrop: #e4e5e8;
  }
  * { box-sizing: border-box; margin: 0; padding: 0; }
  html, body {
    width: 1200px; height: 900px; overflow: hidden;
    background: var(--backdrop);
    font-family: "Arimo", Arial, sans-serif;
  }
  .sheet {
    width: 1200px; height: 900px;
    display: flex; align-items: center; justify-content: center; gap: 40px;
  }
  .card {
    width: 540px; height: 309px;
    border-radius: 3px;
    box-shadow: 0 6px 18px rgba(0,0,0,0.18);
    position: relative;
    overflow: hidden;
  }
  .card--front { background: var(--paper); display: flex; align-items: center; }
  .card--back { background: var(--navy); display: flex; align-items: center; justify-content: center; }

  .brand { display: flex; flex-direction: column; }
  .brand__row { display: flex; align-items: center; gap: 10px; }
  .brand__dot { border-radius: 50%; flex: none; }
  .brand__name { font-weight: 700; text-transform: uppercase; line-height: 1.05; letter-spacing: 0.5px; }
  .brand__tagline {
    display: flex; align-items: center; gap: 8px;
    margin-top: 8px;
    font-size: 10px; text-transform: uppercase; letter-spacing: 1px;
  }
  .brand__tagline::before { content: ""; flex: 1; height: 1px; }
  .brand__slogan { margin-top: 6px; font-size: 11px; font-weight: 700; letter-spacing: 0.5px; text-transform: uppercase; text-align: right; }

  .card--front .brand { width: 250px; padding: 0 28px 0 30px; align-self: flex-start; margin-top: 56px; }
  .card--front .brand__dot { width: 16px; height: 16px; background: var(--navy); }
  .card--front .brand__name { color: var(--navy); font-size: 22px; }
  .card--front .brand__tagline { color: var(--red); }
  .card--front .brand__tagline::before { background: var(--red); }
  .card--front .brand__slogan { color: var(--navy); }

  .card--back .brand { width: 300px; }
  .card--back .brand__dot { width: 24px; height: 24px; background: #fff; }
  .card--back .brand__name { color: #fff; font-size: 34px; }
  .card--back .brand__tagline { color: #fff; font-size: 12px; }
  .card--back .brand__tagline::before { background: #fff; }
  .card--back .brand__slogan { color: #fff; font-size: 13px; }

  .divider { width: 1px; height: 200px; background: var(--rule); flex: none; }

  .details { padding-left: 24px; color: var(--grey-text); font-size: 13px; line-height: 1.3; }
  .details__name { color: var(--navy); font-weight: 700; font-size: 19px; text-transform: uppercase; letter-spacing: 0.3px; }
  .details__title { margin-top: 3px; font-size: 13px; }
  .details__address { margin-top: 14px; }
  .contact-list { list-style: none; margin-top: 14px; }
  .contact-list li { display: flex; align-items: center; gap: 8px; margin-bottom: 2px; }
  .contact-list svg { width: 11px; height: 11px; flex: none; fill: none; stroke: var(--red); stroke-width: 2; }
</style>
</head>
<body>
<main class="sheet">
  <section class="card card--front" aria-label="Card front">
    <div class="brand">
      <div class="brand__row">
        <span class="brand__dot"></span>
        <span class="brand__name">Cedar Ridge<br>Paving</span>
      </div>
      <p class="brand__tagline">Over 40 Years</p>
      <p class="brand__slogan">Chip Seal Done Right</p>
    </div>
    <div class="divider"></div>
    <div class="details">
      <p class="details__name">Mark T. Delgado</p>
      <p class="details__title">Operations Manager</p>
      <p class="details__address">2400 Ranch Road 12<br>Suite 210, Wimberley, TX 78676</p>
      <ul class="contact-list">
        <li>
          <svg viewBox="0 0 24 24"><path d="M5 3h4l2 5-3 2a12 12 0 0 0 6 6l2-3 5 2v4a2 2 0 0 1-2 2A18 18 0 0 1 3 5a2 2 0 0 1 2-2z"/></svg>
          +1 512.408.7316
        </li>
        <li>
          <svg viewBox="0 0 24 24"><rect x="6" y="2" width="12" height="20" rx="2"/><path d="M11 18h2"/></svg>
          +1 512.408.7390
        </li>
        <li>
          <svg viewBox="0 0 24 24"><rect x="2" y="5" width="20" height="14" rx="1"/><path d="M2 6l10 7 10-7"/></svg>
          Markdelgado7@mailbrook.net
        </li>
        <li>
          <svg viewBox="0 0 24 24"><circle cx="12" cy="12" r="10"/><path d="M2 12h20M12 2a15 15 0 0 1 0 20M12 2a15 15 0 0 0 0 20"/></svg>
          www.cedarridgepaving.net
        </li>
      </ul>
    </div>
  </section>

  <section class="card card--back" aria-label="Card back">
    <div class="brand">
      <div class="brand__row">
        <span class="brand__dot"></span>
        <span class="brand__name">Cedar Ridge<br>Paving</span>
      </div>
      <p class="brand__tagline">Over 40 Years</p>
      <p class="brand__slogan">Chip Seal Done Right</p>
    </div>
  </section>
</main>
</body>
</html>
```